BRIGHTDESK - Remote Tech Support Site

We are looking for a new very responsive and simple website for our brand Brightdesk.com - a remote technical support company.

This company supports customers Globally in different countries throughout Eur/ North America / South America / Asia etc (please keep this in mind and integrate into the idea).

Its important to us that the design is very explanatory, the customer should easily be able to figure out that we provide computer support right away ... I like one page responsive type designs as well without a bunch of menu items

Here are some similar sites we like - but still looking for a unique design that fits out brand "brightdesk" - I have upload also some layouts i like (but the designs are not important just the layouts), youll see it includes consumer business etc which is important.

VOLM.COM - I love how clean it is - nice and white easy to see everything

PLUMWIRE247.COM - also nice the layout and responsive one page design makes it easy to use

corvalfix.com - similar to plumwire design as well - you can get the idea im looking for between the two

You will notice those examples are much different then the attachments I added - again this is more of an idea for possible layouts .. attached is also the logo - could inspire color scheme / blue white black etc

Target Market(s)

Home consumers without computer knowledge , older age 45-65, small medium business ... computer repair - slow computers

Industry/Entity Type

Computer Repair

Logo Text

Brightdesk

Coding

Coded - Design and coding required

Number of Pages Required

1 page

Font styles to use
Sans Serif
Other font styles liked:
• your choice responsive

Colors

Designer to choose colors to be used in the design.

Requirements
Must have
• Clean - responsive - professional design - the name says it all - brightdesk
• CALL TO ACTIONS FOR "Get Help Now!" / "Learn More" etc
Nice to have
• We are looking for a new very responsive and simple website for our brand Brightdesk.com - a remote technical support company.
• This company supports customers Globally in different countries throughout Eur/ North America / South America / Asia etc (please keep this in mind and integrate into the idea).
• Its important to us that the design is very explanatory, the customer should easily be able to figure out that we provide computer support right away ... I like one page responsive type designs as well without a bunch of menu items
• Here are some similar sites we like - but still looking for a unique design that fits out brand "brightdesk" - I have upload also some layouts i like (but the designs are not important just the layouts), youll see it includes consumer business etc which is important.
• VOLM.COM - I love how clean it is - nice and white easy to see everything
• PLUMWIRE247.COM - also nice the layout and responsive one page design makes it easy to use
• corvalfix.com - similar to plumwire design as well - you can get the idea im looking for between the two
Should not have
• dark, packed page - bad small font -

```html
<!DOCTYPE html>
<html lang="en">
<head>
<meta charset="utf-8">
<title>Brightdesk – Remote Tech Support</title>
<link rel="stylesheet" href="https://fonts.googleapis.com/css2?family=Oswald:wght@300;400;500;700&family=Roboto+Condensed:wght@400;700&display=swap">
<style>
:root{
  --blue:#1e90f0;
  --yellow:#ffc62a;
  --teal:#2fc7c9;
  --green:#48c95a;
  --ink:#2b2b2b;
  --black:#111;
  --grey:#5a5a5a;
  --light:#efefef;
  --white:#fff;
}
*{margin:0;padding:0;box-sizing:border-box}
html,body{width:1200px;height:2496px;overflow:hidden}
body{position:relative;background:var(--light);font-family:"Oswald",sans-serif;color:var(--ink)}
.abs{position:absolute}
.pill{position:absolute;display:flex;align-items:center;justify-content:center;border-radius:40px;text-decoration:none;font-family:"Oswald",sans-serif}

/* header */
.site-header{position:absolute;left:0;top:0;width:1200px;height:76px;background:#f3f3f3}
.brand{position:absolute;left:61px;top:16px;display:flex;align-items:center;gap:8px}
.brand-dot{width:42px;height:42px;border-radius:50%;background:var(--blue)}
.brand-name{font-family:"Oswald",sans-serif;font-weight:400;font-size:31px;color:var(--blue);line-height:1}
.main-nav a{position:absolute;top:27px;font-size:15px;color:#333;text-decoration:none;text-transform:uppercase}
.contact{position:absolute;top:21px;display:flex;align-items:center;gap:10px;font-family:"Roboto Condensed",sans-serif;font-size:13px;color:#444}
.contact-icon{width:32px;height:32px;border-radius:50%;background:#6d6d6d;display:flex;align-items:center;justify-content:center}

/* hero */
.hero-photo{left:0;top:76px;width:1200px;height:594px;background:linear-gradient(90deg,#ececec 0%,#e0e0e0 40%,#bdbdbd 70%,#d2d2d2 100%)}
.hero-title{left:61px;top:196px;font-size:44px;line-height:54px;color:#555;text-transform:uppercase}
.hero-title b{font-weight:700;display:block}
.hero-title span{font-weight:300;display:block}
.hero-list{list-style:none;position:absolute;top:337px;font-family:"Roboto Condensed",sans-serif;font-size:16px;color:#555;text-transform:uppercase}
.hero-list li{display:flex;align-items:center;gap:14px;height:35px}
.chev{width:13px;height:13px;border-radius:50%;background:var(--blue);display:flex;align-items:center;justify-content:center}
.btn-hero{left:61px;top:476px;width:229px;height:61px;background:var(--blue);color:#fff;font-size:27px;font-weight:400}

/* intro split */
.intro-blue{left:0;top:670px;width:598px;height:456px;background:linear-gradient(135deg,#2aa0ff,#1a86e8)}
.intro-yellow{left:598px;top:670px;width:602px;height:456px;background:linear-gradient(135deg,#ffd03e,#ffbe1c)}
.intro-title{left:0;width:598px;top:695px;text-align:center;color:#fff;font-weight:500;font-size:58px}
.intro-sub{left:54px;top:776px;font-weight:300;font-size:26px;color:#fff}
.intro-rule{left:54px;top:830px;width:452px;height:2px;background:#fff}
.intro-text{left:54px;top:882px;width:510px;font-family:"Roboto Condensed",sans-serif;font-size:15.5px;line-height:21px;color:#fff}
.intro-text p+p{margin-top:20px}
.feat-title{left:598px;width:555px;top:698px;text-align:center;font-weight:500;font-size:44px;color:var(--ink)}
.feat-sub{left:598px;width:555px;top:758px;text-align:center;font-weight:300;font-size:26px;color:var(--ink)}
.feature{position:absolute;height:60px;display:flex;align-items:center}
.feature-icon{width:62px;height:62px;border-radius:50%;background:var(--black);border:3px solid #fff;display:flex;align-items:center;justify-content:center;position:relative;z-index:1}
.feature-label{margin-left:-14px;height:32px;width:225px;padding-left:26px;background:var(--black);color:#fff;border-radius:0 18px 18px 0;display:flex;align-items:center;font-size:16px;text-transform:uppercase;font-weight:300}
.btn-grab{left:786px;top:1043px;width:230px;height:63px;background:var(--blue);color:#fff;font-size:27px}

/* pricing */
.pricing-title{left:0;width:1200px;top:1160px;text-align:center;color:var(--blue);font-weight:700;font-size:41px}
.pricing-sub{left:0;width:1200px;top:1221px;text-align:center;font-family:"Roboto Condensed",sans-serif;font-weight:700;font-size:13.5px;color:var(--black)}
.plan{position:absolute;background:#fff;text-align:center}
.plan-name{font-weight:500;font-size:43px;line-height:1;color:var(--ink)}
.plan-price{margin-top:14px;font-weight:500;font-size:46px;line-height:1;color:var(--blue)}
.plan-price small{font-size:30px;font-weight:400}
.plan-price em{font-style:normal;font-size:16px;font-weight:500;position:relative;top:8px}
.plan-fee{margin-top:16px;font-family:"Roboto Condensed",sans-serif;font-weight:700;font-size:13px}
.plan-rule{margin:10px auto 0;width:248px;height:1px;background:#333}
.plan-feats{margin-top:8px;font-family:"Roboto Condensed",sans-serif;font-size:13px;line-height:16px;text-transform:uppercase}
.plan-feats b{display:block}
.plan-extra{display:block;margin-top:9px;color:var(--blue);font-weight:700}
.plan-btn{position:relative;margin:14px auto 0;width:132px;height:28px;border-radius:16px;background:var(--black);color:#fff;display:flex;align-items:center;justify-content:center;font-family:"Roboto Condensed",sans-serif;font-weight:700;font-size:12px;text-decoration:none}
.plan-featured{background:#2e2e2e;color:#fff}
.plan-featured .plan-name{color:#fff}
.plan-featured .plan-price,.plan-featured .plan-fee,.plan-featured .plan-feats{color:var(--yellow)}
.plan-featured .plan-rule{background:var(--yellow)}
.plan-featured .plan-btn{background:var(--yellow);color:var(--black)}

/* how it works / benefits */
.how-bg{left:0;top:1646px;width:598px;height:452px;background:linear-gradient(135deg,#3ad2d0,#27bcc4)}
.benefit-bg{left:600px;top:1646px;width:600px;height:452px;background:linear-gradient(135deg,#52d25e,#3fc052)}
.how-title{left:84px;top:1683px;font-weight:500;font-size:38px;color:#fff}
.step{position:absolute;left:61px;display:flex;gap:26px;width:520px}
.step-icon{flex:none;width:56px;height:56px;border-radius:50%;background:#fff;display:flex;align-items:center;justify-content:center}
.step h3{font-family:"Roboto Condensed",sans-serif;font-weight:700;font-size:14px;color:#fff;text-transform:uppercase}
.step p{margin-top:4px;font-family:"Roboto Condensed",sans-serif;font-size:15.5px;line-height:20px;color:#fff}
.btn-yellow{background:var(--yellow);color:var(--black);font-size:29px}
.benefit-title{left:618px;top:1666px;font-weight:500;font-size:38px;line-height:50px;color:#fff}
.benefit-list{list-style:none;position:absolute;left:626px;top:1805px;font-family:"Roboto Condensed",sans-serif;font-size:16px;color:#fff}
.benefit-list li{display:flex;align-items:center;gap:24px;height:41px}
.btn-black{background:var(--black);color:#fff;font-size:29px}

/* member band */
.member-band{left:0;top:2098px;width:1200px;height:179px;background:var(--yellow)}
.member-price{left:54px;top:2129px;font-weight:500;font-size:82px;line-height:1;color:var(--black)}
.member-cta{left:640px;width:500px;top:2130px;text-align:center;font-weight:500;font-size:37px;color:var(--black)}

/* footer */
.site-footer{position:absolute;left:0;top:2277px;width:1200px;height:219px;background:#ededed}
.foot-col{position:absolute;top:30px}
.foot-col h4{font-weight:500;font-size:23px;color:var(--black);padding-bottom:6px;border-bottom:1px solid #555}
.foot-links{list-style:none;margin-top:12px;font-family:"Roboto Condensed",sans-serif;font-size:16px;color:#333}
.foot-links li{height:32px}
.foot-note{margin-top:10px;font-family:"Roboto Condensed",sans-serif;font-size:11px;color:#333}
.foot-input{margin-top:12px;width:219px;height:34px;background:#7a7a7a;color:#fff;font-family:"Roboto Condensed",sans-serif;font-size:15px;padding:7px 8px}
.foot-submit{margin-top:8px;width:118px;height:32px;background:var(--black);color:#fff;font-family:"Roboto Condensed",sans-serif;font-size:15px;display:flex;align-items:center;justify-content:center}
.badge-rating{position:absolute;left:0;top:72px;width:141px;height:46px;border-radius:3px;background:#7bcf8e}
.badge-secure{position:absolute;left:174px;top:63px;width:117px;height:73px;border-radius:14px;background:#3a3a3a}
.social{position:absolute;top:68px;width:28px;height:28px;border-radius:50%;background:#222}
</style>
</head>
<body>

<header class="site-header">
  <div class="brand"><span class="brand-dot"></span><span class="brand-name">brightdesk</span></div>
  <nav class="main-nav">
    <a style="left:393px" href="#">Home</a>
    <a style="left:456px" href="#">About Bright</a>
    <a style="left:553px" href="#">Support</a>
    <a style="left:635px" href="#">Services</a>
    <a style="left:717px" href="#">Contact</a>
  </nav>
  <div class="contact" style="left:861px">
    <span class="contact-icon"><svg width="16" height="12" viewBox="0 0 16 12"><rect x="0.5" y="0.5" width="15" height="11" fill="none" stroke="#fff"/><path d="M1 1l7 6 7-6" fill="none" stroke="#fff"/></svg></span>
    info@brightdesk.com
  </div>
  <div class="contact" style="left:1033px">
    <span class="contact-icon"><svg width="14" height="14" viewBox="0 0 14 14"><path d="M3 1l2.5 3-1.5 1.5c.8 1.8 2.2 3.2 4 4L9.5 8 13 10.5 11.5 13C6 12.5 1.5 8 1 2.5z" fill="#fff"/></svg></span>
    (555) 014-2280
  </div>
</header>

<section class="hero">
  <div class="abs hero-photo" role="img" aria-label="Grayscale photo of a smiling support technician working at a laptop"></div>
  <h1 class="abs hero-title"><b>Dedicated Support</b><span>Anytime, Anywhere.</span></h1>
  <ul class="hero-list" style="left:61px">
    <li><span class="chev"><svg width="7" height="7" viewBox="0 0 7 7"><path d="M2 1l3 2.5L2 6" fill="none" stroke="#fff" stroke-width="1.5"/></svg></span>Instant support</li>
    <li><span class="chev"><svg width="7" height="7" viewBox="0 0 7 7"><path d="M2 1l3 2.5L2 6" fill="none" stroke="#fff" stroke-width="1.5"/></svg></span>Real time optimization</li>
    <li><span class="chev"><svg width="7" height="7" viewBox="0 0 7 7"><path d="M2 1l3 2.5L2 6" fill="none" stroke="#fff" stroke-width="1.5"/></svg></span>Free dianostic</li>
  </ul>
  <ul class="hero-list" style="left:361px">
    <li><span class="chev"><svg width="7" height="7" viewBox="0 0 7 7"><path d="M2 1l3 2.5L2 6" fill="none" stroke="#fff" stroke-width="1.5"/></svg></span>Quick setup &amp; install</li>
    <li><span class="chev"><svg width="7" height="7" viewBox="0 0 7 7"><path d="M2 1l3 2.5L2 6" fill="none" stroke="#fff" stroke-width="1.5"/></svg></span>Leading security software</li>
    <li><span class="chev"><svg width="7" height="7" viewBox="0 0 7 7"><path d="M2 1l3 2.5L2 6" fill="none" stroke="#fff" stroke-width="1.5"/></svg></span>Unlimited cloud backup</li>
  </ul>
  <a class="pill btn-hero" href="#">Get support now</a>
</section>

<section class="intro">
  <div class="abs intro-blue" role="img" aria-label="Blue-tinted photo of hands typing on a laptop"></div>
  <div class="abs intro-yellow" role="img" aria-label="Yellow-tinted photo of a family using a computer together"></div>
  <h2 class="abs intro-title">BRIGHTDESK</h2>
  <p class="abs intro-sub">DEDICATED SUPPORT... ANYTIME, ANYWHERE</p>
  <div class="abs intro-rule"></div>
  <div class="abs intro-text">
    <p>Our team is a leader in providing top notch quality services and products with a focus on our customer's needs. We are happy to discuss your computer issues and provide a free valuable diagnostic to determine the best solutions.</p>
    <p>While you are looking for the best source out there, we have everything for your computer and internet security!</p>
  </div>

  <h2 class="abs feat-title">ALL THE BEST FEATURES</h2>
  <p class="abs feat-sub">AT THE BEST PRICE!</p>
  <div class="feature" style="left:646px;top:822px">
    <span class="feature-icon"><svg width="34" height="34" viewBox="0 0 34 34"><circle cx="17" cy="17" r="14" fill="none" stroke="#fff" stroke-width="4"/><path d="M7 7l20 20" stroke="#fff" stroke-width="4"/></svg></span>
    <span class="feature-label">Add blocker</span>
  </div>
  <div class="feature" style="left:920px;top:824px">
    <span class="feature-icon"><svg width="32" height="30" viewBox="0 0 32 30"><rect x="3" y="18" width="5" height="10" fill="#fff"/><rect x="11" y="13" width="5" height="15" fill="#fff"/><rect x="19" y="9" width="5" height="19" fill="#fff"/><path d="M3 12l9-6 6 3 10-7" fill="none" stroke="#fff" stroke-width="2"/></svg></span>
    <span class="feature-label" style="width:220px">Regular tune-ups</span>
  </div>
  <div class="feature" style="left:646px;top:922px">
    <span class="feature-icon"><svg width="32" height="30" viewBox="0 0 32 30"><rect x="2" y="3" width="28" height="19" rx="2" fill="none" stroke="#fff" stroke-width="2.5"/><path d="M12 27h8M16 22v5" stroke="#fff" stroke-width="2.5"/><circle cx="16" cy="12" r="4" fill="none" stroke="#fff" stroke-width="2"/></svg></span>
    <span class="feature-label">Sytem reports</span>
  </div>
  <div class="feature" style="left:920px;top:924px">
    <span class="feature-icon"><svg width="32" height="32" viewBox="0 0 32 32"><rect x="11" y="2" width="10" height="8" fill="none" stroke="#fff" stroke-width="2"/><rect x="2" y="22" width="10" height="8" fill="none" stroke="#fff" stroke-width="2"/><rect x="20" y="22" width="10" height="8" fill="none" stroke="#fff" stroke-width="2"/><path d="M16 10v6M7 22v-6h18v6" fill="none" stroke="#fff" stroke-width="2"/></svg></span>
    <span class="feature-label" style="width:220px">Multiple devices</span>
  </div>
  <a class="pill btn-grab" href="#">Grab More now !</a>
</section>

<section class="pricing">
  <h2 class="abs pricing-title">MEMBERSHIP PRICING AND PLANS</h2>
  <p class="abs pricing-sub">FREE OPTIMIZATION AND DIAGNOSTIC WHEN YOU CALL IN. LIMITED TIME OFFER.</p>

  <article class="plan" style="left:61px;top:1284px;width:358px;height:294px;padding-top:24px">
    <h3 class="plan-name">PREMIUM</h3>
    <div class="plan-price">$19.99 <small>/</small> <em>MONTHLY</em></div>
    <div class="plan-fee">( $249-$300 SETUP FEE )</div>
    <div class="plan-rule"></div>
    <div class="plan-feats">Regular 90-day optimization<b>Unlimited 24/7 tier 3 technician support</b></div>
    <div class="plan-rule"></div>
    <a class="plan-btn" href="#">LEARN MORE</a>
  </article>

  <article class="plan plan-featured" style="left:420px;top:1262px;width:361px;height:331px;padding-top:20px">
    <h3 class="plan-name">PREMIUM PLUS</h3>
    <div class="plan-price">$29.99 <small style="color:#fff">/</small> <em>MONTHLY</em></div>
    <div class="plan-fee">( $249-$300 SETUP FEE )</div>
    <div class="plan-rule"></div>
    <div class="plan-feats">Regular 90-day optimization<b>Unlimited 24/7 tier 3 technician support</b></div>
    <div class="plan-rule"></div>
    <a class="plan-btn" href="#">LEARN MORE</a>
  </article>

  <article class="plan" style="left:781px;top:1284px;width:360px;height:340px;padding-top:24px">
    <h3 class="plan-name">PLATINUM</h3>
    <div class="plan-price">$39.99 <small>/</small> <em>MONTHLY</em></div>
    <div class="plan-fee">( $249-$300 SETUP FEE )</div>
    <div class="plan-rule"></div>
    <div class="plan-feats">Regular 90-day optimization<b>Unlimited 24/7 tier 3 technician support</b><span class="plan-extra">Online identity theft protection</span></div>
    <div class="plan-rule"></div>
    <a class="plan-btn" href="#" style="margin-top:30px">LEARN MORE</a>
  </article>
</section>

<section class="how">
  <div class="abs how-bg" role="img" aria-label="Teal-tinted photo of a support agent wearing a headset"></div>
  <div class="abs benefit-bg" role="img" aria-label="Green-tinted photo of a woman smiling at her laptop"></div>
  <h2 class="abs how-title">HOW IT WORKS</h2>
  <div class="step" style="top:1765px">
    <span class="step-icon"><svg width="30" height="26" viewBox="0 0 30 26"><rect x="1" y="1" width="28" height="18" rx="2" fill="none" stroke="var(--teal)" stroke-width="2.5"/><path d="M10 25h10M15 19v6M4 11h6l2-4 3 8 3-6 2 2h6" fill="none" stroke="var(--teal)" stroke-width="2"/></svg></span>
    <div><h3>Free diagnostic</h3><p>Get a diagnostic, FOR FREE! Get a free consultation with our staff.</p></div>
  </div>
  <div class="step" style="top:1848px">
    <span class="step-icon"><svg width="30" height="30" viewBox="0 0 30 30"><path d="M5 25L20 10M20 10a5 5 0 1 0 0-.1" fill="none" stroke="var(--teal)" stroke-width="4" stroke-linecap="round"/><path d="M6 5l19 19" stroke="var(--teal)" stroke-width="4" stroke-linecap="round"/></svg></span>
    <div><h3>Get fixed</h3><p>Get fixed, IMMEDIATELY! Our staff will solve your computer issues right before your eyes</p></div>
  </div>
  <div class="step" style="top:1932px">
    <span class="step-icon"><svg width="32" height="28" viewBox="0 0 32 28"><path d="M8 22a6 6 0 0 1 0-12 9 9 0 0 1 17 2 5 5 0 0 1 0 10z" fill="none" stroke="var(--teal)" stroke-width="2.5"/><path d="M16 26V14M12 18l4-4 4 4" fill="none" stroke="var(--teal)" stroke-width="2.5"/></svg></span>
    <div><h3>Backup your information</h3><p>Saving your files is now EASY! You will be able to retain your personal files without any loss of data.</p></div>
  </div>
  <a class="pill btn-yellow" href="#" style="left:174px;top:2017px;width:231px;height:62px">Read More</a>

  <h2 class="abs benefit-title">REAL TIME<br>SUPPORT FEATURES AND BENEFITS</h2>
  <ul class="benefit-list">
    <li><svg width="18" height="14" viewBox="0 0 18 14"><path d="M2 1l6 6-6 6M9 1l6 6-6 6" fill="none" stroke="#fff" stroke-width="2"/></svg>24/7 Real-Time Technician Support</li>
    <li><svg width="18" height="14" viewBox="0 0 18 14"><path d="M2 1l6 6-6 6M9 1l6 6-6 6" fill="none" stroke="#fff" stroke-width="2"/></svg>The best Security Software in the market</li>
    <li><svg width="18" height="14" viewBox="0 0 18 14"><path d="M2 1l6 6-6 6M9 1l6 6-6 6" fill="none" stroke="#fff" stroke-width="2"/></svg>Regular tune-ups and optimization</li>
    <li><svg width="18" height="14" viewBox="0 0 18 14"><path d="M2 1l6 6-6 6M9 1l6 6-6 6" fill="none" stroke="#fff" stroke-width="2"/></svg>Setup and installation included</li>
  </ul>
  <a class="pill btn-black" href="#" style="left:768px;top:2009px;width:230px;height:64px">Become a member</a>
</section>

<section class="member">
  <div class="abs member-band"></div>
  <p class="abs member-price">$19.99/ MONTH</p>
  <h2 class="abs member-cta">BCOME A MEMBER TODAY</h2>
  <a class="pill btn-black" href="#" style="left:744px;top:2194px;width:232px;height:63px">Read More</a>
</section>

<footer class="site-footer">
  <div class="foot-col" style="left:67px;width:148px">
    <h4>PLANS</h4>
    <ul class="foot-links"><li>Premium Plan</li><li>Premium Plus Plan</li><li>Platinum plan</li></ul>
  </div>
  <div class="foot-col" style="left:260px;width:225px">
    <h4>NEWSLETTER SINGUP</h4>
    <p class="foot-note">Sign up for our regular informational newsletters</p>
    <div class="foot-input">Enter your e-mail Id</div>
    <div class="foot-submit">Submit</div>
  </div>
  <div class="foot-col" style="left:543px;width:305px">
    <h4>TRUSTED BY</h4>
    <span class="badge-rating" role="img" aria-label="Customer rating badge"></span>
    <span class="badge-secure" role="img" aria-label="Secure site certificate badge"></span>
  </div>
  <div class="foot-col" style="left:927px;width:213px">
    <h4>FOLLOW US</h4>
    <span class="social" style="left:3px" role="img" aria-label="Social profile link"></span>
    <span class="social" style="left:47px" role="img" aria-label="Social profile link"></span>
  </div>
</footer>

</body>
</html>
```